Hockey Youth Club - Complete HP Design

I need a complete homepage design for a new youth hockey club. There are already some elements that can be used. For more information, please visit this products webpage. This site is currently unavailable for purchase at this time (Current) -) Team (Players, Coaches, Crew) -) Club (Philiosophy , Rules, Management Board, ....) -) Partners (Sponsors, Partners, ...)) Contact (Contact details, Callback Button) -) Shop (in the beginning view of products - further planned as online shop ) -) .... probably 2-3 more -) Footer with social media info, ..... Homepages from other youth hockey clubs (ex. Www.brel. At - this is what I am looking for in my life - BUT we dont want to copy them !!! Im interested in new and innovative designs.
Updates

Project Deadline Extended
Reason: Too much Wordpress - no innovation - please offer more designs in dark concept. At the moment the design is too decent - we are looking for sporty, active and fresh design. Thank you

Target Market(s)

Youth Hockey Players Parents

Industry/Entity Type

Club

Number of Pages Required

5+ page

Colors
fbed38
9d9d9d
1b1b1b
f5f5f5
ffffff

Requirements
Must have
• Clearline, modern design,
Nice to have
• Flashing elements (maybe the scratches fading in ...)
Should not have
• chaos

```html
<!DOCTYPE html>
<html lang="en">
<head>
<meta charset="utf-8">
<title>Stripeclaws Youth Hockey Club</title>
<link rel="stylesheet" href="https://fonts.googleapis.com/css2?family=Khand:wght@500;600;700&family=Open+Sans:wght@400;600;700&display=swap">
<style>
:root{
  --yellow:#fbed38;
  --gold:#f6cf1f;
  --grey:#9d9d9d;
  --ink:#1b1b1b;
  --panel:#333333;
  --smoke:#f5f5f5;
  --white:#ffffff;
  --sky:#6ec3ea;
  --card-dark:rgba(60,60,60,.88);
}
*{margin:0;padding:0;box-sizing:border-box}
html,body{width:1200px;height:3109px;overflow:hidden}
body{position:relative;background:var(--white);font-family:"Open Sans",Arial,sans-serif;color:var(--ink)}
.abs{position:absolute}

/* hero + arena backdrop */
.arena-bg{left:0;top:0;width:1200px;height:1600px;
  background:
    radial-gradient(ellipse 260px 90px at 880px 640px,rgba(120,40,40,.55),rgba(0,0,0,0) 70%),
    radial-gradient(ellipse 700px 160px at 600px 760px,rgba(170,180,215,.35),rgba(0,0,0,0) 70%),
    radial-gradient(ellipse 500px 220px at 1050px 1000px,rgba(200,210,235,.45),rgba(0,0,0,0) 70%),
    radial-gradient(ellipse 500px 260px at 150px 1250px,rgba(40,50,90,.55),rgba(0,0,0,0) 70%),
    linear-gradient(180deg,#000 0%,#030303 30%,#11141d 38%,#2c3452 44%,#4b5580 52%,#5d6894 62%,#56608c 72%,#6d78a3 80%,#9aa2c2 86%,#fff 100%)}
.hero-player{left:560px;top:200px;width:560px;height:460px;
  background:
    radial-gradient(ellipse 150px 110px at 300px 120px,rgba(235,235,235,.9),rgba(160,160,160,.45) 45%,rgba(0,0,0,0) 100%),
    radial-gradient(ellipse 220px 120px at 320px 270px,rgba(70,70,70,.9),rgba(25,25,25,.7) 55%,rgba(0,0,0,0) 100%),
    radial-gradient(ellipse 280px 210px at 290px 220px,rgba(150,150,150,.45),rgba(0,0,0,0) 100%)}
.ice-edge{left:0;top:1270px}

.brand{left:87px;top:40px;display:flex;align-items:center;gap:10px}
.brand-mark{width:46px;height:46px;background:var(--yellow);border-radius:50%}
.brand-name{font-family:"Khand",sans-serif;font-weight:700;font-size:34px;color:var(--yellow);line-height:1}

.main-nav{left:667px;top:10px;width:533px;height:48px;background:#151515;
  font-family:"Khand",sans-serif;font-weight:600;font-size:14px;color:var(--yellow);letter-spacing:.5px}
.main-nav a{position:absolute;top:15px;color:var(--yellow);text-decoration:none}
.login{position:absolute;left:426px;top:14px;width:66px;height:24px;background:var(--yellow);color:var(--ink);
  text-align:center;line-height:26px;font-size:13px}

.hero-title{left:257px;top:188px;font-family:"Khand",sans-serif;font-weight:700;color:var(--white);line-height:.9}
.hero-title .we{font-size:112px;letter-spacing:-2px}
.hero-title .small{font-size:58px}
.hero-title .game{display:block;font-size:118px;color:var(--yellow);margin-top:-6px}
.hero-title .changers{display:block;font-size:58px;margin-top:-4px}

.section-title{font-family:"Khand",sans-serif;font-weight:700;letter-spacing:10px;text-align:center}
.team-title{left:0;width:1200px;top:852px;font-size:34px;color:var(--gold)}

.event{width:377px;height:338px}
.event-photo{width:100%;height:213px;background:linear-gradient(135deg,#e9eef3,#c7d3df 55%,#d9442a 56%,#b23b2a 70%,#dfe6ee)}
.event-foot{height:125px;background:var(--gold);display:flex;padding:10px 14px;gap:14px}
.event-date{font-family:"Khand",sans-serif;font-weight:700;color:var(--white);font-size:60px;line-height:.8;text-align:center;padding-top:8px}
.event-h{font-family:"Khand",sans-serif;font-weight:700;font-size:18px;line-height:1.1}
.event-p{font-size:11px;font-weight:600;line-height:1.3}
.note{width:259px;height:158px;background:var(--card-dark);padding:18px 22px;color:var(--white)}
.note .event-h{color:var(--yellow)}
.event-small{width:259px;height:338px}
.event-small .event-photo{height:213px;position:relative;background:linear-gradient(135deg,#8fb8c8,#c7d8e2 45%,#e25a22 46%,#c14a20 65%,#dbe6ee)}
.event-small .event-date{position:absolute;left:16px;top:70px;color:var(--ink);font-size:64px}
.event-small .event-foot{display:block}
.next-arrow{left:1070px;top:1060px}

/* shop */
.shop-title{left:522px;top:1617px;width:158px;height:43px;border:2px solid var(--ink);font-size:22px;line-height:44px;padding-left:10px}
.product{background:var(--panel);padding:11px}
.product.lite{background:var(--gold);padding:13px}
.product-img{background:linear-gradient(160deg,#f2f2f2,#c9cfd8 50%,#3d5f9c 80%,#c9343a)}
.product.lite .product-img{background:linear-gradient(150deg,#fff 0%,#f0f0f0 30%,#c8202c 55%,#222 80%,#fff)}
.product-img.plain{background:linear-gradient(160deg,#f7f7f7,#bdbdbd)}
.p-name{position:absolute;font-family:"Khand",sans-serif;font-weight:700;color:var(--gold);line-height:.95}
.product.lite .p-name{color:var(--ink)}
.p-price{position:absolute;font-family:"Khand",sans-serif;font-weight:700;color:var(--gold)}
.product.lite .p-price{color:var(--ink)}
.p-cart{position:absolute;font-family:"Khand",sans-serif;font-weight:600;font-size:12px;color:var(--white)}
.product.lite .p-cart{color:var(--ink)}
.p-more{position:absolute;font-size:9px;font-weight:600;color:var(--white)}
.product.lite .p-more{color:var(--ink)}
.view-all{left:545px;top:2172px;width:112px;height:25px;background:var(--panel);color:var(--white);
  font-family:"Khand",sans-serif;font-weight:600;font-size:12px;letter-spacing:4px;text-align:center;line-height:26px}

/* follow */
.follow-bg{left:0;top:2270px;width:1200px;height:550px;
  background:
    radial-gradient(ellipse 260px 160px at 120px 170px,rgba(255,255,255,.9),rgba(255,255,255,0) 70%),
    radial-gradient(ellipse 300px 160px at 1080px 200px,rgba(255,255,255,.8),rgba(255,255,255,0) 70%),
    linear-gradient(180deg,#fff 0%,#c9cccf 14%,#b9bdc2 45%,#cfd2d5 78%,#fff 100%)}
.follow-player{left:500px;top:2290px;width:480px;height:440px;
  background:
    radial-gradient(ellipse 70px 60px at 210px 70px,rgba(235,238,240,.95),rgba(255,255,255,0) 100%),
    radial-gradient(ellipse 170px 190px at 240px 230px,rgba(140,148,156,.75),rgba(190,195,200,.35) 60%,rgba(255,255,255,0) 100%)}
.frost-top{left:0;top:2270px}
.frost-bottom{left:0;top:2700px}
.follow-title{left:0;width:1200px;top:2355px;font-size:26px;color:var(--ink)}
.label{font-family:"Khand",sans-serif;font-weight:700;font-size:14px;letter-spacing:4px}
.wall{left:290px;top:2477px;width:280px;height:183px;background:var(--white);box-shadow:0 1px 4px rgba(0,0,0,.2)}
.wall-cover{height:108px;background:linear-gradient(120deg,#4a5a6a,#b49a6e 50%,#7b5a3e)}
.wall-name{position:absolute;left:58px;top:8px;color:var(--white);font-weight:700;font-size:15px}
.wall-sq{position:absolute;left:10px;top:40px;width:40px;height:40px;background:var(--white)}
.wall-text{padding:8px 10px;font-size:10px;color:#555}
.wall-faces{margin:4px 10px;height:26px;background:linear-gradient(90deg,#9aa,#c9b,#abc,#bca,#9ab)}
.chirp{left:640px;top:2473px;width:256px;height:180px;background:var(--sky);padding:16px 24px;color:var(--ink);font-size:12.5px;font-weight:600;line-height:1.3}
.chirp-tail{left:640px;top:2653px}
.chirp-btn{position:absolute;left:15px;top:127px;width:110px;height:29px;background:var(--yellow);font-family:"Khand",sans-serif;
  font-weight:600;font-size:14px;text-align:center;line-height:30px}

/* footer */
.foot-col{font-family:"Khand",sans-serif;font-weight:600;font-size:14px;letter-spacing:2px;text-align:center;line-height:25px}
.foot-col .hl{color:var(--gold);letter-spacing:4px}
.foot-rule{width:2px;height:125px;background:var(--ink)}
</style>
</head>
<body>

<div class="abs arena-bg" role="img" aria-label="Dark hockey arena with crowded blue-lit stands"></div>
<div class="abs hero-player" role="img" aria-label="Hockey player skating hard through a burst of ice spray"></div>

<svg class="abs ice-edge" width="1200" height="330" viewBox="0 0 1200 330" role="img" aria-label="Ice spray fading into white">
  <defs>
    <linearGradient id="iceFade" x1="0" y1="0" x2="0" y2="1">
      <stop offset="0" stop-color="#fff" stop-opacity=".55"/>
      <stop offset=".45" stop-color="#fff" stop-opacity=".92"/>
      <stop offset="1" stop-color="#fff"/>
    </linearGradient>
  </defs>
  <path d="M0 60 C60 20 110 120 170 70 C230 20 260 150 330 110 C400 70 430 170 500 140 C560 115 600 190 660 150 C720 110 760 180 830 130 C900 80 930 170 1000 120 C1060 80 1110 150 1200 90 L1200 330 L0 330 Z" fill="url(#iceFade)"/>
  <path d="M0 150 C80 120 140 210 220 170 C300 130 360 230 440 200 C520 170 580 250 660 215 C740 180 800 250 880 210 C960 170 1040 240 1120 200 C1160 180 1180 190 1200 180 L1200 330 L0 330 Z" fill="#fff"/>
</svg>

<div class="abs brand"><span class="brand-mark"></span><span class="brand-name">STRIPECLAWS</span></div>

<nav class="abs main-nav">
  <a style="left:56px">TEAM</a>
  <a style="left:131px">CLUB</a>
  <a style="left:208px">PARTNERS</a>
  <a style="left:283px">CONTACT</a>
  <a style="left:357px">SHOP</a>
  <span class="login">LOGIN</span>
</nav>

<h1 class="abs hero-title"><span class="we">WE</span><span class="small">ARE THE</span><span class="game">GAME</span><span class="changers">CHANGERS</span></h1>

<h2 class="abs section-title team-title">OUR TEAM</h2>

<article class="abs event" style="left:104px;top:937px">
  <div class="event-photo" role="img" aria-label="Youth players chasing the puck on the ice"></div>
  <div class="event-foot">
    <div class="event-date">15<br>Jun</div>
    <div><div class="event-h">Lorem ipsum dolor sit amet</div>
    <p class="event-p">Consectetur adipiscing elit. Mauris lobortis ex quis augue laoreet, et scelerisque justo mollis. Nam convallis dapibus dui, ultricies vestibulum velit tempus in. Phasellus porta massa sit amet eros ultricies, maximus</p></div>
  </div>
</article>

<article class="abs note" style="left:500px;top:937px">
  <div class="event-h">Lorem ipsum dolor sit amet</div>
  <p class="event-p">Consectetur adipiscing elit. Mauris lobortis ex quis augue laoreet, et scelerisque justo mollis. Nam convallis dapibus dui, ultricies vestibulum velit tempus in. Phasellus porta massa sit amet</p>
</article>
<article class="abs note" style="left:500px;top:1115px">
  <div class="event-h">Lorem ipsum dolor sit amet</div>
  <p class="event-p">Consectetur adipiscing elit. Mauris lobortis ex quis augue laoreet, et scelerisque justo mollis. Nam convallis dapibus dui, ultricies vestibulum velit tempus in. Phasellus porta massa sit amet</p>
</article>

<article class="abs event-small" style="left:771px;top:937px">
  <div class="event-photo" role="img" aria-label="Young player in orange skating with the puck">
    <div class="event-date">05<br>Jun</div>
  </div>
  <div class="event-foot">
    <div class="event-h">Lorem ipsum dolor sit amet</div>
    <p class="event-p">Consectetur adipiscing elit. Mauris lobortis ex quis augue laoreet, et scelerisque justo mollis. Nam convallis dapibus dui, ultricies vestibulum velit tempus in. Phasellus porta massa sit amet</p>
  </div>
</article>

<svg class="abs next-arrow" width="36" height="64" viewBox="0 0 36 64" aria-label="Next"><polyline points="6,4 30,32 6,60" fill="none" stroke="#fff" stroke-width="5"/></svg>

<h2 class="abs section-title shop-title">SHOP</h2>

<article class="abs product" style="left:166px;top:1710px;width:302px;height:438px">
  <div class="product-img" style="height:290px" role="img" aria-label="White event t-shirt with star-spangled print"></div>
  <div class="p-name" style="left:24px;top:322px;font-size:30px">SEASON 11<br>TSHIRT</div>
  <div class="p-more" style="left:26px;top:388px">View Details</div>
  <div class="p-price" style="left:229px;top:322px;font-size:30px">$20</div>
  <div class="p-cart" style="left:220px;top:380px">ADD TO CART</div>
</article>

<article class="abs product lite" style="left:497px;top:1710px;width:195px;height:214px">
  <div class="product-img" style="height:149px" role="img" aria-label="Pair of red and black hockey gloves"></div>
  <div class="p-name" style="left:13px;top:170px;font-size:26px">GLOVES</div>
  <div class="p-more" style="left:13px;top:196px">View Details</div>
  <div class="p-price" style="left:143px;top:166px;font-size:26px">$20</div>
  <div class="p-cart" style="left:128px;top:194px;font-size:10px">ADD TO CART</div>
</article>
<article class="abs product lite" style="left:497px;top:1936px;width:195px;height:212px">
  <div class="product-img" style="height:149px" role="img" aria-label="Pair of red and black hockey gloves"></div>
  <div class="p-name" style="left:13px;top:168px;font-size:26px">GLOVES</div>
  <div class="p-more" style="left:13px;top:194px">View Details</div>
  <div class="p-price" style="left:143px;top:164px;font-size:26px">$20</div>
  <div class="p-cart" style="left:128px;top:192px;font-size:10px">ADD TO CART</div>
</article>

<article class="abs product" style="left:727px;top:1710px;width:309px;height:438px">
  <div class="product-img plain" style="height:290px" role="img" aria-label="White t-shirt with sailboat print"></div>
  <div class="p-name" style="left:26px;top:322px;font-size:30px">SEASON 03<br>TSHIRT</div>
  <div class="p-more" style="left:28px;top:388px">View Details</div>
  <div class="p-price" style="left:231px;top:322px;font-size:30px">$20</div>
  <div class="p-cart" style="left:222px;top:380px">ADD TO CART</div>
</article>

<div class="abs view-all">VIEW ALL</div>

<div class="abs follow-bg" role="img" aria-label="Frosted ice backdrop with bright rink lights"></div>
<div class="abs follow-player" role="img" aria-label="Faded hockey player skating with stick"></div>
<svg class="abs frost-top" width="1200" height="120" viewBox="0 0 1200 120" aria-hidden="true">
  <path d="M0 0 L1200 0 L1200 40 C1120 80 1060 20 980 60 C900 100 840 30 760 70 C680 105 620 40 540 75 C460 110 400 40 320 80 C240 115 170 45 90 85 C50 100 20 80 0 90 Z" fill="#fff"/>
</svg>
<svg class="abs frost-bottom" width="1200" height="120" viewBox="0 0 1200 120" aria-hidden="true">
  <path d="M0 50 C70 20 130 80 210 45 C290 10 350 75 430 40 C510 8 580 70 660 35 C740 5 810 70 890 40 C970 10 1040 70 1120 35 C1160 20 1180 30 1200 25 L1200 120 L0 120 Z" fill="#fff"/>
</svg>
<h2 class="abs section-title follow-title">FOLLOW US</h2>

<div class="abs label" style="left:303px;top:2448px">FRIENDWALL</div>
<div class="abs wall">
  <div class="wall-cover" role="img" aria-label="Club page cover photo"></div>
  <span class="wall-sq"></span>
  <span class="wall-name">Friendwall</span>
  <p class="wall-text">Join the club wall today</p>
  <div class="wall-faces" role="img" aria-label="Row of member thumbnails"></div>
</div>

<div class="abs label" style="left:649px;top:2448px">CHIRPLINE</div>
<div class="abs chirp">
  <p>Lorem ipsum dolor sit amet Consectetur adipiscing elit. Mauris lobortis ex quis augue laoreet, et scelerisque justo mollis. Nam convallis dapibus dui, ultricies</p>
  <span class="chirp-btn">TO CHIRPLINE</span>
</div>
<svg class="abs chirp-tail" width="20" height="16" viewBox="0 0 20 16"><polygon points="0,0 20,0 4,16" fill="#6ec3ea"/></svg>

<footer>
  <div class="abs foot-col" style="left:187px;top:2865px;width:120px">HOME<br>TEAM<br>CLUB<br>PARTNERS<br>SHOP<br>CONTACT</div>
  <span class="abs foot-rule" style="left:358px;top:2860px"></span>
  <div class="abs foot-col" style="left:409px;top:2865px;width:160px"><span class="hl">FOLLOW US</span><br>FRIENDWALL &nbsp;-<br>CHIRPLINE &nbsp;-</div>
  <span class="abs foot-rule" style="left:662px;top:2860px"></span>
  <div class="abs foot-col" style="left:745px;top:2865px;width:180px"><span class="hl">ADDRESS</span><br>D.NO-123,<br>STREET,<br>CITY,<br>COUNTRY-12345</div>
  <div class="abs foot-col" style="left:961px;top:2865px;width:200px">CONTACT<br><span style="line-height:18px;display:block">PHONE:123-456-789<br>EMAIL: MAIL@COM</span></div>
</footer>

</body>
</html>
```